International Medical Company Needs a Website Design for a Support Site

We need a website design for a support site we are doing for ostomates called Bright Returns. We are an international company but this website is for our Australian market.

The website is a support site for people who are living with an Ostomy or Bowel Disease. This is a site where they can read other ostomates' stories and how they are dealing with the fact that they have to wear a pouch everyday.

The URL for our US site is: http://www.brightreturnsvale.com/

We need to use the same logo but we have freedom around the color scheme. We are not fond of the brown color scheme used in our US site and are happy for designs to be submitted with alternatives.

• We want the design to be clean, inspiring, modern and inviting.
• We would like to see a design for the mainpage / homepage and one of the subpages
• We only require the PSD / image files (no HTML needed)

Attached to this project is our sitemap, an example wireframe and the logos. We are happy for you to play around with different options and don't have to stick to the layout shown in the wireframe.

If you have any further questions please ask.

```html
<!DOCTYPE html>
<html lang="en">
<head>
<meta charset="utf-8">
<title>Bright Returns – Sharing Stories and Giving Hope</title>
<link href="https://fonts.googleapis.com/css2?family=Roboto:wght@400;500;700&display=swap" rel="stylesheet">
<style>
:root{
  --blue:#2c5f88;
  --blue-dark:#24506f;
  --green:#4caf45;
  --green-nav:#5cb554;
  --green-dark:#3e9638;
  --text:#2b2b2b;
  --muted:#666;
  --line:#d5d9dd;
  --white:#fff;
  --page:#ffffff;
}
*{box-sizing:border-box;margin:0;padding:0}
html,body{width:708px;height:1200px;overflow:hidden;background:var(--page)}
body{font-family:'Roboto',Arial,sans-serif;color:var(--text);font-size:8px;position:relative}
a{color:inherit;text-decoration:none}

/* top bar */
.topbar{height:15px;background:var(--blue);color:var(--white);font-size:7px;font-weight:700;display:flex;align-items:center;justify-content:space-between;padding:0 58px}
.topbar .call{display:flex;align-items:center;gap:5px}
.topbar .call i{width:9px;height:9px;border-radius:50%;background:var(--green);display:inline-block}
.country{display:flex;align-items:center;gap:6px}
.country span.select{background:var(--white);color:var(--text);width:52px;height:10px;padding:0 3px;font-weight:400;display:flex;justify-content:space-between;align-items:center}

/* header */
.header{height:60px;display:flex;align-items:center;justify-content:space-between;padding:0 59px}
.logo{display:flex;align-items:center;gap:6px;color:var(--blue);font-weight:700;font-size:12px;letter-spacing:.3px;margin-top:14px}
.logo i{width:16px;height:16px;border-radius:50%;background:var(--blue);display:block}
.btn{display:inline-flex;align-items:center;justify-content:center;font-weight:700;font-size:8px;color:var(--white);text-transform:uppercase;border-radius:2px}
.btn-green{background:var(--green)}
.btn-blue{background:var(--blue)}
.header .btn{width:110px;height:18px;margin-top:-14px}

/* nav */
.nav{height:23px;background:var(--green-nav);border-top:1px solid var(--green-dark);display:flex;align-items:center;padding:0 59px}
.nav ul{list-style:none;display:flex;height:100%}
.nav li{color:var(--white);font-size:8px;font-weight:500;padding:0 10px;display:flex;align-items:center;border-right:1px solid rgba(255,255,255,.35)}
.nav li:first-child{border-left:1px solid rgba(255,255,255,.35)}
.nav li.active{background:var(--blue)}
.search{margin-left:auto;display:flex;align-items:center;gap:6px;color:var(--white);font-weight:700;font-size:7px}
.search span.field{width:110px;height:13px;background:var(--white);display:flex;align-items:center;justify-content:space-between;padding:0 4px;color:var(--muted);font-weight:400;font-size:6.5px}

/* hero */
.hero{position:relative;height:297px;background:linear-gradient(90deg,#e9e6e2 0%,#f3f2f0 55%,#eeeeee 100%);overflow:hidden}
.hero-photo{position:absolute;left:50px;top:0;width:330px;height:297px;background:radial-gradient(ellipse at 45% 55%,#e7c2a4 0%,#d7a982 35%,#b9ab9d 65%,rgba(233,230,226,0) 100%)}
.hero-copy{position:absolute;left:400px;top:58px;width:250px}
.hero-copy h1{font-weight:400;font-size:19px;color:#3a3a3a;margin-bottom:10px}
.hero-copy p{font-size:7px;line-height:11px;color:#333;margin-bottom:9px}
.hero-actions{display:flex;align-items:center;gap:8px;margin-top:16px}
.hero-actions .btn{width:102px;height:20px}
.or{width:18px;height:18px;border-radius:50%;border:1px solid #999;background:#fff;font-size:7px;display:flex;align-items:center;justify-content:center;color:#555}
.arrow{position:absolute;top:132px;width:21px;height:21px;background:#9a9a9a;display:flex;align-items:center;justify-content:center}
.arrow.left{left:16px}.arrow.right{right:16px}

/* section title */
.section-title{text-align:center;font-weight:500;font-size:11px;color:#222;padding-top:22px;height:46px;border-bottom:1px solid var(--line);margin:0 59px}

/* cards */
.card{position:absolute;background:var(--white);border:1px solid #cfd4d8;border-bottom:3px solid var(--blue);box-shadow:0 1px 3px rgba(0,0,0,.15)}
.card h2{background:var(--blue);color:var(--white);font-size:8px;font-weight:700;text-align:center;height:16px;line-height:16px;text-transform:uppercase}
.card-body{padding:6px 8px;font-size:7px;line-height:10px}
.thumb{border:1px solid #ccc;padding:2px;background:#fff;margin-bottom:6px}
.thumb div{height:100%}
.card .more{display:block;margin:6px auto 0;width:62px;height:14px;border:1px solid #aaa;border-radius:2px;text-align:center;line-height:12px;font-size:7px;background:#fafafa}
.green-text{color:var(--green);font-weight:500}
.green-link{color:var(--green);font-style:italic;font-weight:700}
.news-item{display:flex;gap:6px;margin-bottom:7px}
.date{width:20px;height:24px;background:var(--green);color:#fff;font-weight:700;font-size:6px;text-align:center;line-height:9px;padding-top:3px;flex:none;border-bottom:2px solid var(--green-dark)}
.resource{display:flex;gap:8px;margin-bottom:14px}
.badge{width:66px;height:58px;border:1px solid #ccc;flex:none;display:flex;align-items:center;justify-content:center}
.resource p{font-size:6.6px;line-height:9.4px}
.resource h3{font-size:7px;color:var(--green);font-weight:500;margin-bottom:2px}

/* footer */
.footer{position:absolute;left:0;top:1059px;width:708px;height:141px;background:var(--blue);color:var(--white)}
.footer-cols{display:flex;padding:18px 0 0 58px;height:120px}
.fcol{font-size:7px;line-height:12px;padding-right:10px;border-right:1px solid rgba(255,255,255,.2);margin-right:10px}
.fcol h4{font-size:7px;font-weight:700;margin-bottom:5px;text-transform:uppercase}
.fcol ul{list-style:none;color:#cfdde8}
.map{width:105px;height:62px;background:linear-gradient(135deg,#e8e4d8,#cfd9c4 60%,#e4dcc8);border:2px solid #fff}
.nl input{display:none}
.field-w{width:130px;height:14px;background:#fff;color:#333;font-size:7px;padding:0 5px;line-height:14px;margin-bottom:4px;font-weight:500}
.nl-row{display:flex}
.nl-row .field-w{width:96px}
.nl-row .btn{width:34px;height:14px}
.copy-bar{height:21px;background:var(--blue-dark);display:flex;align-items:center;justify-content:space-between;padding:0 58px 0 58px;font-size:7px;font-weight:500}
.social{display:flex;align-items:center;gap:3px}
.social i{width:11px;height:11px;display:block;background:#5a87b3}
.social i:nth-child(2){background:#4aa3d8}.social i:nth-child(3){background:#3a6fa8}.social i:nth-child(4){background:#8a8a8a}.social i:nth-child(5){background:#c8322b}
</style>
</head>
<body>

<div class="topbar">
  <div class="call"><i></i>CALL : 123.456.7890</div>
  <div class="country">Choose Your Country : <span class="select">Australia <svg width="6" height="4"><path d="M0 0h6L3 4z" fill="#333"/></svg></span></div>
</div>

<header class="header">
  <div class="logo"><i></i>BRIGHT RETURNS</div>
  <a class="btn btn-green">Share a Story</a>
</header>

<nav class="nav">
  <ul>
    <li class="active">Home</li><li>About Us</li><li>Personal Stories</li><li>Tips for Living</li><li>News</li><li>Resources</li><li>Contact Us</li>
  </ul>
  <div class="search">SEARCH : <span class="field">Enter text here <svg width="8" height="8"><circle cx="3.2" cy="3.2" r="2.4" fill="none" stroke="#4caf45" stroke-width="1.2"/><path d="M5 5l2.5 2.5" stroke="#4caf45" stroke-width="1.3"/></svg></span></div>
</nav>

<section class="hero">
  <div class="hero-photo" role="img" aria-label="Photo of a smiling mother hugged from behind by her young daughter"></div>
  <div class="arrow left"><svg width="8" height="10"><path d="M7 0v10L0 5z" fill="#fff"/></svg></div>
  <div class="arrow right"><svg width="8" height="10"><path d="M1 0v10l7-5z" fill="#fff"/></svg></div>
  <div class="hero-copy">
    <h1>Sharing Stories and Giving Hope</h1>
    <p>Lorem ipsum dolor sit amet consectetur incididunt ut labore et dolore magna aliqua adipisicing elit seddo eiusmod tempor. Sed perspiciatis unde omniste natus error voluptatem remops accusantium.</p>
    <p>Lorem ipsum dolor sit amet consectetur incididunt ut labore et dolore magna aliqua adipisicing elit seddo eiusmod tempor.</p>
    <div class="hero-actions">
      <a class="btn btn-blue">Read More Stories</a><span class="or">or</span><a class="btn btn-green" style="width:100px">Share a Story</a>
    </div>
  </div>
</section>

<h2 class="section-title">Bright Returns Shining Bright</h2>

<article class="card" style="left:59px;top:466px;width:178px;height:220px">
  <h2>What is Bright Returns</h2>
  <div class="card-body">
    <div class="thumb" style="height:78px"><div role="img" aria-label="Program banner with a soaring bird over bright sky" style="background:linear-gradient(180deg,#3f6fb0,#9cc2e6 60%,#d7e6f2)"></div></div>
    <p>The Bright Returns® Program began in 1984 under the leadership of Carl Westholm, with support from Medivale. It was designed to raise awareness of quality of life issues for people living with Crohn's disease, ulcerative colitis, colorectal cancer or other diseases that can lead to ostomy surgery.</p>
    <a class="more">Read More</a>
  </div>
</article>

<article class="card" style="left:264px;top:466px;width:178px;height:220px">
  <h2>Share a Story</h2>
  <div class="card-body">
    <div class="thumb" style="height:78px"><div role="img" aria-label="Portrait photo of award recipient standing by a tree" style="background:linear-gradient(90deg,#5d5a3e,#8a8a60 50%,#3e3a2f)"></div></div>
    <p class="green-text">Mara Ellison</p>
    <p>1999 Bright Returns® Award Recipient</p>
    <p style="margin-top:6px">Mara Ellison has always been up for a challenge, be it juggling time between work and family, participating in a charity walkathon or living with the daily challenges of IBD. <span class="green-link">Read More</span></p>
    <a class="more" style="width:70px">Read All Stories</a>
  </div>
</article>

<article class="card" style="left:471px;top:466px;width:178px;height:220px">
  <h2>Latest News</h2>
  <div class="card-body">
    <div class="thumb" style="height:76px"><div role="img" aria-label="Photo of letter dice spelling news" style="background:linear-gradient(180deg,#cfd3d6,#9da2a6)"></div></div>
    <div class="news-item"><div class="date">21<br>AUG</div><p>Bright Returns® Recognizes Former Principal, Dean Halvorsen, As National Award Recipient</p></div>
    <div class="news-item"><div class="date">21<br>AUG</div><p>Dean Halvorsen of Fairmont, MD Receives 2012 Bright Returns® East Region Award</p></div>
    <a class="more" style="width:70px;margin-top:2px">Read All News</a>
  </div>
</article>

<article class="card" style="left:59px;top:713px;width:298px;height:303px">
  <h2>US Awards Programs</h2>
  <div class="card-body" style="padding:6px 9px">
    <div class="thumb" style="height:90px"><div role="img" aria-label="Photo of a glass eagle award trophy" style="background:radial-gradient(ellipse at 55% 55%,#d9d4cc,#8a7a6a 55%,#4a3f35)"></div></div>
    <p>Whether your dream is to start a business, make the varsity basketball team or teach kindergarten – your journey can be an inspiration to others!</p>
    <p style="margin-top:8px">Each year, the Bright Returns® Advisory Committee recognizes inspirational individuals of all ages who, by sharing their personal stories, give hope and encouragement so that others can reclaim their lives and pursue their dreams. Anyone who has overcome the challenges of living with serious intestinal diseases and ostomy surgery can share their story. Friends, family members and healthcare professionals can also nominate someone for an award.</p>
    <p style="margin-top:8px">We hope that you will share your story with us!</p>
    <a class="more" style="margin-top:9px">Read More</a>
  </div>
</article>

<article class="card" style="left:384px;top:713px;width:265px;height:303px">
  <h2>US Links / Resources</h2>
  <div class="card-body">
    <div class="resource">
      <div class="badge"><svg width="34" height="40"><rect width="34" height="40" fill="#5b3d7a"/></svg></div>
      <div><h3>The Bowel Health Alliance (BHA)</h3>
      <p>The Bowel Health Alliance (BHA) mission is to cure Crohn's disease and ulcerative colitis, and to improve the quality of life of children and adults affected by these diseases. The Foundation ranks third among leading health non-profits in the percentage of expense devoted to research toward a cure, with more than 79 cents of every dollar the Foundation spends going to mission-critical programs.<br><b><i>Visit : <span class="green-text">www.bhalliance.org</span></i></b> <span class="green-link" style="float:right">Read More</span></p></div>
    </div>
    <div class="resource">
      <div class="badge"><svg width="44" height="30"><circle cx="15" cy="15" r="13" fill="#2c5f88"/><rect x="30" y="9" width="12" height="12" fill="#2c5f88"/></svg></div>
      <div><h3>The Allied Ostomy Groups, Inc. (AOG)</h3>
      <p>The Allied Ostomy Groups, Inc. (AOG) is a national network for bowel and urinary diversion support groups in the United States. Its goal is to provide a non-profit association that will serve to unify and strengthen its member support groups, which are organized for the benefit of people who have, or will have intestinal or urinary diversions and their caregivers. For more information, please<br><b><i>Visit : <span class="green-text">www.alliedostomy.org</span></i></b></p></div>
    </div>
    <a class="more" style="margin-top:-4px">View All</a>
  </div>
</article>

<footer class="footer">
  <div class="footer-cols">
    <div class="fcol" style="width:71px"><h4>Company</h4><ul><li>Home</li><li>AboutUs</li><li>Stories</li><li>News</li><li>Contact</li></ul></div>
    <div class="fcol" style="width:90px"><h4>Links</h4><ul><li>Resources</li><li>Awards Programs</li><li>Legal Notice</li><li>Privacy Policy</li><li>Sitemap</li></ul></div>
    <div class="fcol" style="width:128px"><h4>Contact Us</h4><ul><li>ABCD Energy Company</li><li>Abc Building,</li><li>12345 Australia</li><li>P : +123 456 7890</li><li>E : info@brightreturnsvale.com</li></ul></div>
    <div class="fcol" style="width:132px"><h4>Find Us on the Map</h4><div class="map" role="img" aria-label="Small street map showing the office location"></div></div>
    <div class="fcol nl" style="border:none"><h4>Sign Up for Newsletter</h4>
      <div class="field-w">First Name</div><div class="field-w">Last Name</div>
      <div class="nl-row"><div class="field-w">Email Address</div><a class="btn btn-green">Submit</a></div>
    </div>
  </div>
  <div class="copy-bar">
    <span>Copyright © 2014 Bright Returns</span>
    <span class="social">Social Media&nbsp;<i></i><i></i><i></i><i></i><i></i></span>
  </div>
</footer>

</body>
</html>
```